Super elegant, crisp & clean Business card design required

We recently upgraded our branding - which is on our website - tavorelstudio.com

I would like a simple, yet elegant, clean business card design please.

The font of my logo is Cinzel - and because of the natural colour - it's best to have this on a black background.

I would like to have the back of the business card - with simply my logo.

PLEASE DO NOT SUBMIT A COMPLICATED / UNCLEAN DESIGN

Industry/Entity Type

Business

Contact Information for Business Card

Dalvik Ostrander Photography

Font styles to use
Other font styles liked:
• Cinzel

Requirements
Must have
• A backpage with nothing but my logo
• Simple design - stands out
Should not have
• Colour that dont align with my logo
• Over complicated '/ non symmetrical design

```html
<!DOCTYPE html>
<html lang="en">
<head>
<meta charset="utf-8">
<title>Dalvik Ostrander Photography – Business Card</title>
<link href="https://fonts.googleapis.com/css2?family=Cinzel:wght@400&display=swap" rel="stylesheet">
<style>
  :root {
    --backdrop: #857661;
    --card: #060102;
    --gold: #7a6a4f;
  }
  * { margin: 0; padding: 0; box-sizing: border-box; }
  html, body { width: 952px; height: 1200px; overflow: hidden; }
  body {
    background: var(--backdrop);
    position: relative;
    font-family: "Cinzel", serif;
    color: var(--gold);
  }
  .card {
    position: absolute;
    background: var(--card);
  }
  .card__frame {
    position: absolute;
    inset: 14px;
    border: 2px solid var(--gold);
  }
  .card--front { left: 107px; top: 117px; width: 745px; height: 426px; }
  .card--back  { left: 106px; top: 643px; width: 754px; height: 431px; }

  .brand {
    position: absolute;
    left: 0; right: 0;
    text-align: center;
    line-height: 1;
  }
  .brand__name { display: block; white-space: nowrap; }
  .brand__tagline {
    display: block;
    letter-spacing: 0.95em;
    margin-right: -0.95em;
  }
  .card--front .brand { top: 296px; }
  .card--front .brand__name { font-size: 45px; }
  .card--front .brand__tagline { font-size: 17px; margin-top: 6px; }

  .brand-mark {
    position: absolute;
    left: 50%;
    top: 76px;
    width: 170px;
    height: 170px;
    margin-left: -85px;
    border: 2px solid var(--gold);
    border-radius: 50%;
  }

  .card--back .brand { top: 62px; }
  .card--back .brand__name { font-size: 53px; }
  .card--back .brand__tagline { font-size: 21px; margin-top: 4px; }

  .contact {
    position: absolute;
    left: 194px;
    width: 366px;
    top: 219px;
    list-style: none;
    border-top: 2px solid var(--gold);
  }
  .contact__item {
    height: 51px;
    border-bottom: 2px solid var(--gold);
    display: flex;
    align-items: center;
    justify-content: center;
    font-size: 18px;
    letter-spacing: 0.02em;
  }
</style>
</head>
<body>
  <section class="card card--front">
    <div class="card__frame"></div>
    <div class="brand-mark" aria-hidden="true"></div>
    <div class="brand">
      <span class="brand__name">Dalvik Ostrander</span>
      <span class="brand__tagline">Photography</span>
    </div>
  </section>

  <section class="card card--back">
    <div class="card__frame"></div>
    <div class="brand">
      <span class="brand__name">Dalvik Ostrander</span>
      <span class="brand__tagline">Photography</span>
    </div>
    <ul class="contact">
      <li class="contact__item">ph: 555 555 555</li>
      <li class="contact__item">www.yourwebsite.com</li>
      <li class="contact__item">youremail@.email.com</li>
    </ul>
  </section>
</body>
</html>
```